Quillory Nest Business Card

I need a business card design. We are a collaborate online training company. Our colors are gray and green. Our website is QuilloryNest.com

I would like an area for a profile picture within the card

```html
<!DOCTYPE html>
<html lang="en">
<head>
<meta charset="utf-8">
<title>Quillory Nest Business Card</title>
<link rel="stylesheet" href="https://fonts.googleapis.com/css2?family=Source+Sans+3:wght@400;600;700&display=swap">
<style>
  :root {
    --stage: #e7e7e4;
    --card: #ffffff;
    --card-shade: #ececec;
    --green: #8cc63f;
    --green-light: #c6e49a;
    --ink: #2b2b2b;
    --gray: #6b6b6b;
    --photo-dark: #4a4a4c;
    --photo-light: #d9d9db;
  }
  * { box-sizing: border-box; margin: 0; padding: 0; }
  html, body {
    width: 1200px; height: 843px; overflow: hidden;
    background: var(--stage);
    font-family: "Source Sans 3", "Myriad Pro", Arial, sans-serif;
  }
  .canvas { position: relative; width: 1200px; height: 843px; }
  .card {
    position: absolute; width: 560px; height: 320px;
    background: linear-gradient(160deg, var(--card) 40%, var(--card-shade) 100%);
    box-shadow: 0 6px 18px rgba(0,0,0,.18);
    overflow: hidden;
  }

  /* front */
  .card-front { left: 60px; top: 70px; }
  .profile-photo {
    position: absolute; left: 40px; top: 40px; width: 200px; height: 280px;
    background: linear-gradient(180deg, var(--photo-light) 0%, #8a8a8d 45%, var(--photo-dark) 100%);
  }
  .front-brand { position: absolute; left: 262px; top: 140px; }
  .wordmark {
    display: flex; align-items: center; gap: 10px;
    font-size: 40px; font-weight: 700; color: var(--ink); letter-spacing: -1px; line-height: 1;
  }
  .wordmark .dot { width: 18px; height: 18px; border-radius: 50%; background: var(--green); flex: none; }
  .front-brand .site { margin: 4px 0 0 120px; font-size: 20px; color: var(--gray); letter-spacing: 1px; }

  /* back */
  .card-back { left: 580px; top: 450px; }
  .name-band {
    position: absolute; left: 0; top: 40px; width: 560px; height: 62px;
    background: linear-gradient(90deg, var(--green) 0%, var(--green) 45%, var(--green-light) 75%, rgba(255,255,255,0) 100%);
  }
  .name-band .name { position: absolute; left: 40px; top: 8px; color: #fff; font-size: 21px; font-weight: 600; line-height: 1.1; }
  .name-band .role { position: absolute; left: 40px; top: 32px; color: #fff; font-size: 15px; }
  .back-brand { position: absolute; right: 28px; top: 94px; }
  .back-brand .wordmark { font-size: 34px; }
  .back-brand .dot { width: 22px; height: 22px; }
  .contacts { position: absolute; left: 36px; top: 196px; list-style: none; }
  .contacts li { display: flex; align-items: center; gap: 10px; font-size: 17px; color: var(--gray); line-height: 24px; }
  .contacts svg { width: 14px; height: 14px; flex: none; }
  .address {
    position: absolute; right: 34px; bottom: 26px; text-align: right;
    font-size: 17px; line-height: 22px; color: var(--gray); font-style: normal;
  }
</style>
</head>
<body>
<main class="canvas">
  <section class="card card-front">
    <div class="profile-photo" role="img" aria-label="Profile photo of the founder"></div>
    <div class="front-brand">
      <div class="wordmark"><span class="dot"></span>QuilloryNest</div>
      <div class="site">quillorynest.com</div>
    </div>
  </section>

  <section class="card card-back">
    <div class="name-band">
      <div class="name">Dorian Vell</div>
      <div class="role">Founder</div>
    </div>
    <div class="back-brand">
      <div class="wordmark"><span class="dot"></span>QuilloryNest</div>
    </div>
    <ul class="contacts">
      <li>
        <svg viewBox="0 0 16 16" aria-hidden="true"><path fill="#8cc63f" d="M3.5 1.5l2.5 0 1 3.5-1.6 1.2a8 8 0 0 0 4.4 4.4l1.2-1.6 3.5 1v2.5c0 1-1 1.5-2 1.5A12 12 0 0 1 2 3.5c0-1 .5-2 1.5-2z"/></svg>
        (555) 014-2290
      </li>
      <li>
        <svg viewBox="0 0 16 16" aria-hidden="true"><rect x="1" y="3" width="14" height="10" rx="1" fill="#8cc63f"/><path d="M1.5 3.8L8 9l6.5-5.2" stroke="#fff" stroke-width="1.3" fill="none"/></svg>
        dorian@quillorynest.com
      </li>
      <li>
        <svg viewBox="0 0 16 16" aria-hidden="true"><circle cx="8" cy="8" r="7" fill="#8cc63f"/><path d="M1 8h14M8 1c-3 3.5-3 10.5 0 14M8 1c3 3.5 3 10.5 0 14" stroke="#fff" stroke-width="1" fill="none"/></svg>
        quillorynest.com
      </li>
    </ul>
    <address class="address">
      48 Larkfield Ave.<br>
      Suite 7, Brookmere<br>
      Oregon 97031
    </address>
  </section>
</main>
</body>
</html>
```